Business Card Design Project

We need a business card design for a relatively new company called Velmar Gear. We design paddle (an outdoor winter sport primarily played in the midwest and east coast) and tennis bags for women and men. Velmar Gear is a lifestyle brand for the next generation country club goers. Our bags merge fashion with functionality and are making country club sports trendier and more fashionable.

I would like to include space for
Name: (will fill this in for employees)
Velmar Gear
Phone: (will do this)
Email:
www.velmargear.example

Would also like to include Chatterbook and Flitter icons.
Please do not use pictures of the bags - this is just to give you an idea of what style bags we sell.

Target Market(s)

30 to 40 year old men and women - luxury market

Industry/Entity Type

Fashion

Requirements
Must have
• Would like the company logo included

```html
<!DOCTYPE html>
<html lang="en">
<head>
<meta charset="utf-8">
<title>Velmar Gear – Business Card</title>
<link rel="stylesheet" href="https://fonts.googleapis.com/css2?family=Didact+Gothic&family=Open+Sans:ital,wght@0,400;0,700;1,300&display=swap">
<style>
  :root {
    --stage: #4a4a4a;
    --ink: #000000;
    --paper: #ffffff;
    --brand-red: #d72027;
    --text-dark: #111111;
    --tile: #1a1a1a;
    --ghost: #f2f2f2;
  }
  * { margin: 0; padding: 0; box-sizing: border-box; }
  html, body {
    width: 1200px; height: 892px; overflow: hidden;
    background: var(--stage);
    font-family: "Open Sans", Arial, sans-serif;
  }
  .canvas { position: relative; width: 1200px; height: 892px; }

  .card { position: absolute; overflow: hidden; box-shadow: 0 6px 18px rgba(0,0,0,.45); }

  /* Back card (contact side) */
  .card-back {
    left: 80px; top: 410px; width: 620px; height: 380px;
    background: var(--paper);
  }
  .card-back .ghost-mark {
    position: absolute; left: 330px; top: 60px;
    width: 240px; height: 240px; border-radius: 50%;
    background: var(--ghost);
  }
  .card-back .identity {
    position: absolute; left: 44px; top: 138px;
    font-size: 22px; color: var(--text-dark); white-space: nowrap;
  }
  .identity .person { font-weight: 700; }
  .identity .role { font-style: italic; font-weight: 300; }
  .contact-list { position: absolute; left: 44px; top: 198px; list-style: none; }
  .contact-list li {
    display: flex; align-items: center; gap: 12px;
    font-size: 22px; color: var(--text-dark); line-height: 34px;
  }
  .contact-list svg { width: 30px; height: 22px; flex: none; }
  .social-list { position: absolute; left: 44px; top: 282px; display: flex; gap: 24px; list-style: none; }
  .social-list li { display: flex; align-items: center; gap: 8px; font-size: 18px; font-weight: 700; color: var(--text-dark); }
  .social-list .tile { width: 34px; height: 34px; border-radius: 7px; background: var(--tile); }
  .card-back .base-band {
    position: absolute; left: 0; bottom: 0; width: 100%; height: 38px;
    background: var(--brand-red);
  }

  /* Front card (brand side) */
  .card-front {
    left: 470px; top: 80px; width: 650px; height: 420px;
    background: var(--ink);
  }
  .brand-name {
    position: absolute; left: 0; top: 120px; width: 100%;
    display: flex; align-items: center; justify-content: center; gap: 22px;
    font-family: "Didact Gothic", Arial, sans-serif; font-size: 84px;
    color: var(--paper); white-space: nowrap;
  }
  .brand-name .dot { width: 56px; height: 56px; border-radius: 50%; background: var(--paper); }
  .card-front .web-band {
    position: absolute; left: 0; bottom: 0; width: 100%; height: 112px;
    background: var(--brand-red); border-top: 5px solid var(--paper);
    display: flex; align-items: center; justify-content: center;
    font-size: 30px; font-weight: 700; color: var(--paper);
  }
</style>
</head>
<body>
<main class="canvas">
  <section class="card card-back">
    <div class="ghost-mark" aria-hidden="true"></div>
    <p class="identity"><span class="person">Daniel Reyes</span> - <span class="role">Sales Velmar Gear</span></p>
    <ul class="contact-list">
      <li>
        <svg viewBox="0 0 30 22" aria-hidden="true">
          <path d="M2 8 Q15 0 28 8 L25 12 L20 10 L20 7 Q15 5 10 7 L10 10 L5 12 Z" fill="var(--brand-red)"/>
          <rect x="7" y="12" width="16" height="9" rx="2" fill="var(--brand-red)"/>
          <circle cx="15" cy="16.5" r="2.5" fill="var(--paper)"/>
        </svg>
        0198 442 731
      </li>
      <li>
        <svg viewBox="0 0 30 22" aria-hidden="true">
          <rect x="1" y="3" width="28" height="17" fill="var(--brand-red)"/>
          <path d="M1 3 L15 13 L29 3 M1 20 L11 11 M29 20 L19 11" stroke="var(--paper)" stroke-width="1.8" fill="none"/>
        </svg>
        sales@velmargear.example
      </li>
    </ul>
    <ul class="social-list">
      <li><span class="tile" aria-hidden="true"></span>Flitter</li>
      <li><span class="tile" aria-hidden="true"></span>Chatterbook</li>
    </ul>
    <div class="base-band" aria-hidden="true"></div>
  </section>

  <section class="card card-front">
    <h1 class="brand-name"><span class="dot" aria-hidden="true"></span>Velmar Gear</h1>
    <div class="web-band">www.velmargear.example</div>
  </section>
</main>
</body>
</html>
```